Banner Ad (and potentially other creative assets) designed for a crowdfunding/finance industry association business conference called the 3rd annual Canadian Pooledcapital Forum scheduled for March 1 & 2, 2017.

The conference covers topics around fintech (financial technology), crowdfinance, venture funding markets, online crowdfunding models and alternative finance.

Some words and concepts for reference:
Fintech, Crowdfunding, crowdfinance, investment crowdfunding, securities based crowdfunding, equity crowdfunding, crowdsourcing, reward-based crowdfunding

Startups, small businesses, angel investing, venture capital, online alternative finance, private capital markets, global funding

The design should be fresh, innovative, and jump off the page with excitement around new opportunities for raising capital online for businesses but also a great channel for investors active in venture funding.

Attached are some images and conference banners we used the past for reference.

Links for reference:
Federated Backerfund Council of Canada website (fbcc-hub.example)
Canadian Pooledcapital Forum (pooledforumhub.example)
HarbCAPITAL 2016 (harbcapitalmeet.example)

What: 3rd Annual Canadian Pooledcapital Forum
Date: March 1 & 2, 2017
Location: Orbeline Works Quarter (venue for Day 2 is TBD)
Hashtag: #PPF2017

Fintech Crowdfunding and Alternative Finance Markets
Where the rubber hits the road
Innovation | Entrepreneurship | Investors

Target Market(s)

Startups, scaleups and small businesses, retail investors, angel investors, venture capital, online alternative finance, private capital markets, global funding, international partnerships

Industry/Entity Type

Crowdfunding

Font styles to use
Sans Serif

Colors
9bcb3b
33a6d7
6b449b

Requirements
Must have
• What: 3rd Annual Canadian Pooledcapital Forum
• Day 1: March 1, 2017
• Orbeline Works Quarter
• Day 2: March 2, 2017
• Location TBD
• Fintech Crowdfunding and Alternative Finance Markets
• Innovation | Entrepreneurship | Investors
• #PPF2017
• The design should be fresh, vibrant, dynamic, innovative, tech orientated, and jump off the page with excitement around new opportunities for raising capital online for businesses but also a great channel for investors active in venture funding. This is about bringing emerging fintech and crowdfinance markets TO LIFE!
• Concepts of innovation, technology, finance
Nice to have
• Day 1: Education, Networking, Live Pitching, Exhibitor Showcase
• Day 2: Trade show, Workshops, Meetings, Networking Reception
• Crowd, collaborative, change, impact, Global or international, Transformation, moving forward (progress)

```html
<!DOCTYPE html>
<html lang="en">
<head>
<meta charset="utf-8">
<title>Canadian Pooledcapital Forum – Banner</title>
<link href="https://fonts.googleapis.com/css2?family=Oswald:wght@500;700&family=Open+Sans:wght@400;600;700&display=swap" rel="stylesheet">
<style>
  :root {
    --red: #e5101c;
    --blue: #33a6d7;
    --blue-deep: #1f8fbf;
    --ink: #232323;
    --paper: #ffffff;
    --mist: #efefef;
    --stage: #e9e9e9;
  }
  html, body {
    margin: 0;
    width: 1200px;
    height: 1200px;
    overflow: hidden;
    background: var(--stage);
  }
  .banner {
    position: absolute;
    left: 100px;
    top: 412px;
    width: 1000px;
    height: 375px;
    overflow: hidden;
    background: linear-gradient(90deg, #fafafa 0%, var(--mist) 60%, #f6f6f6 100%);
    font-family: "Open Sans", sans-serif;
  }
  .banner__header-shape {
    position: absolute;
    left: 0; top: 0;
    width: 1000px; height: 375px;
  }
  .brand {
    position: absolute;
    left: 40px;
    top: 26px;
    display: flex;
    align-items: center;
    gap: 18px;
  }
  .brand__dot {
    width: 92px; height: 92px;
    border-radius: 50%;
    background: var(--blue);
    flex: none;
  }
  .brand__title {
    margin: 0;
    line-height: 1;
    text-transform: uppercase;
    font-family: "Oswald", sans-serif;
  }
  .brand__edition {
    display: block;
    font-weight: 500;
    font-size: 12px;
    letter-spacing: 13.4px;
    color: var(--blue-deep);
    margin-bottom: 6px;
  }
  .brand__name {
    display: block;
    font-weight: 700;
    font-size: 33px;
    letter-spacing: 0.5px;
    color: var(--red);
  }
  .brand__tagline {
    position: absolute;
    left: 40px;
    top: 142px;
    margin: 0;
    font-size: 12.5px;
    font-weight: 600;
    color: var(--blue-deep);
  }
  .topic-badge {
    position: absolute;
    left: 54px;
    width: 68px; height: 68px;
    border-radius: 50%;
    border: 3px solid var(--red);
    background: var(--paper);
    display: flex; align-items: center; justify-content: center;
    box-shadow: 0 0 0 2px var(--paper), 0 2px 6px rgba(0,0,0,.15);
  }
  .topic-badge--growth { top: 185px; }
  .topic-badge--currency { top: 271px; }
  .topic-badge__art {
    width: 56px; height: 56px;
    border-radius: 50%;
    border: 3px solid var(--blue);
    box-sizing: border-box;
    background: radial-gradient(circle at 45% 45%, #ffffff 0%, #d9dde2 70%, #b8bec6 100%);
  }
  .event-date {
    position: absolute;
    left: 174px;
    top: 196px;
    margin: 0;
    font-family: "Oswald", sans-serif;
    font-weight: 700;
    font-size: 50px;
    line-height: 1;
    color: var(--ink);
    letter-spacing: -0.5px;
  }
  .event-venue {
    position: absolute;
    left: 175px;
    top: 259px;
    margin: 0;
    font-size: 14px;
    color: var(--red);
  }
  .pillars {
    position: absolute;
    left: 167px;
    top: 290px;
    width: 348px;
    height: 38px;
    border-radius: 19px;
    background: linear-gradient(180deg, #4fb9e4 0%, var(--blue-deep) 100%);
    color: var(--paper);
    font-family: "Oswald", sans-serif;
    font-weight: 500;
    font-size: 18px;
    display: flex; align-items: center; justify-content: center;
    box-shadow: 0 6px 8px -4px rgba(0,0,0,.35);
  }
  .gallery {
    position: absolute;
    left: 571px;
    top: 37px;
    width: 388px;
    height: 287px;
    box-sizing: border-box;
    border: 4px solid var(--blue);
    background: var(--paper);
    display: grid;
    grid-template-columns: repeat(4, 1fr);
    grid-template-rows: repeat(3, 1fr);
    gap: 3px;
    box-shadow: 0 4px 10px rgba(0,0,0,.2);
  }
  .gallery__tile { background: #6c8ba6; }
  .gallery__tile--team-a { background: linear-gradient(160deg, #4d7fa8, #2d4f73); }
  .gallery__tile--team-b { background: linear-gradient(160deg, #6a95bb, #3a6288); }
  .gallery__tile--team-c { background: linear-gradient(160deg, #34597e, #27425f); }
  .gallery__tile--team-d { background: linear-gradient(160deg, #5d7591, #e3e7ec); }
  .gallery__tile--team-e { background: linear-gradient(160deg, #3a4f69, #cfd6df); }
  .gallery__tile--team-f { background: linear-gradient(160deg, #b5bcc6, #eef1f4); }
  .gallery__tile--city-a { background: linear-gradient(180deg, #c9ced3, #4e545a); }
  .gallery__tile--handshake { background: linear-gradient(160deg, #8a9aa6, #3c5f4a); }
  .gallery__tile--desk-a { background: linear-gradient(160deg, #7d858f, #d4d9de); }
  .gallery__tile--desk-b { background: linear-gradient(160deg, #5bb4e5, #cfe9f6); }
  .gallery__tile--desk-c { background: linear-gradient(160deg, #3d3d40, #c9cdd2); }
  .gallery__tile--city-b { background: linear-gradient(180deg, #e5b977, #5a5049); }
  .banner__base {
    position: absolute;
    left: 0; bottom: 0;
    width: 100%; height: 19px;
    background: var(--red);
    display: flex;
    align-items: center;
    justify-content: flex-end;
    box-sizing: border-box;
    padding-right: 41px;
  }
  .hashtag {
    margin: 0;
    font-size: 12px;
    font-weight: 700;
    line-height: 1;
    letter-spacing: 0.5px;
    color: var(--paper);
  }
</style>
</head>
<body>
  <section class="banner" aria-label="Canadian Pooledcapital Forum banner">
    <svg class="banner__header-shape" viewBox="0 0 1000 375" aria-hidden="true">
      <polygon points="0,0 546,0 398,185 111,166 0,185" fill="#ffffff"/>
      <polyline points="0,185 111,166 398,185 546,0" fill="none" stroke="#33a6d7" stroke-width="4"/>
      <polygon points="398,188 404,192 586,0 571,0" fill="#e5101c"/>
    </svg>

    <div class="brand">
      <span class="brand__dot" aria-hidden="true"></span>
      <h1 class="brand__title">
        <span class="brand__edition">3rd Annual</span>
        <span class="brand__name">Canadian</span>
        <span class="brand__name">Pooledcapital</span>
        <span class="brand__name">Forum 2017</span>
      </h1>
    </div>
    <p class="brand__tagline">Fintech Crowdfunding and Alternative Finance Markets</p>

    <div class="topic-badge topic-badge--growth">
      <div class="topic-badge__art" role="img" aria-label="Illustration of a rising bar chart with an upward arrow"></div>
    </div>
    <div class="topic-badge topic-badge--currency">
      <div class="topic-badge__art" role="img" aria-label="Illustration of stacked coins with euro, dollar and pound symbols"></div>
    </div>

    <p class="event-date">MARCH 1 &amp; 2, 2017</p>
    <p class="event-venue">Orbeline Works Quarter (venue for Day 2 is TBD)</p>
    <div class="pillars">INNOVATION | ENTREPRENEURSHIP | INVESTORS</div>

    <div class="gallery">
      <div class="gallery__tile gallery__tile--team-a" role="img" aria-label="Photo of a businessman in a suit looking upward"></div>
      <div class="gallery__tile gallery__tile--team-b" role="img" aria-label="Photo of an office building background"></div>
      <div class="gallery__tile gallery__tile--city-a" role="img" aria-label="Photo of a city skyline in black and white"></div>
      <div class="gallery__tile gallery__tile--handshake" role="img" aria-label="Photo of a business handshake"></div>
      <div class="gallery__tile gallery__tile--team-c" role="img" aria-label="Photo of a smiling businessman"></div>
      <div class="gallery__tile gallery__tile--team-d" role="img" aria-label="Photo of a businesswoman at a meeting"></div>
      <div class="gallery__tile gallery__tile--desk-a" role="img" aria-label="Photo of hands on a laptop"></div>
      <div class="gallery__tile gallery__tile--desk-b" role="img" aria-label="Photo of a person signing documents"></div>
      <div class="gallery__tile gallery__tile--team-e" role="img" aria-label="Photo of business people seated at a desk"></div>
      <div class="gallery__tile gallery__tile--team-f" role="img" aria-label="Photo of a meeting table with papers"></div>
      <div class="gallery__tile gallery__tile--desk-c" role="img" aria-label="Photo of a hand on a keyboard"></div>
      <div class="gallery__tile gallery__tile--city-b" role="img" aria-label="Photo of city towers at sunset"></div>
    </div>

    <div class="banner__base">
      <p class="hashtag">#PPF2017</p>
    </div>
  </section>
</body>
</html>
```